Rest. Build. Thrive. Book Cover

I would like a book cover for the print edition book I am self publishing. My cover will require front, back, and spine design. I have provided a template to assist with sizing and spacing.

My book is named "Rest. Build. Thrive. A Hands-On Diet, Drive to Act, and Attitude Handbook Building Energy Toward Stronger Vitality and Balance" by Gregory Halvorsen RD, CPT. I use the concept of waves as an analogy for forward progress in life and would like that reflected in the cover design. I would like the color scheme to be blacks, whites, grey, and various shades of blue. I have provided a style guide for reference. Please include my logo on the front, spine, and back of the design. Please include an about the author, book summary, and my picture on the back. I have provided the wording below.

About the Author: Gregory Halvorsen is a Registered Dietitian and Certified Personal Trainer from Cleveland, OH. He graduated from the Westbrook Valley University and currently works as a health coach in the healthcare industry. His passions are fitness, nutrition, science, and motivation. He has extensive knowledge and experience in wellness, healthcare, and disease treatment and disease. Gregory has worked with hundreds of people through counseling, consulting, and coaching in an effort to make a difference in their long-term health. In his spare time, he enjoys exercising, watching movies, and trying out new foods.

Book Summary: Believe in you. Trust in You. Rest. Build. Thrive. is a book committed to you. Behavior change and improved health can be challenging. You must feel empowered to make decisions and changes create momentum in the right direction. But, you may not always have the knowledge to do that. This book provides you with practical and fun tools and tips to improve your nutrition, motivation to move, and mindset. You are awesome. You are beautiful. You have the power to control your destiny and future. All you have to do is Rest, Build, and Thrive!

Please use a modern/ futuristic font style for the title. I have also provided some draft book covers for inspiration/ direction. Thank you!

Colors

Designer to choose only greyscale colors for use in the design.

Requirements
Must have
• Color scheme, about author, profile picture, and book summary on back, wave themed graphics

```html
<!DOCTYPE html>
<html lang="en">
<head>
<meta charset="utf-8">
<title>Rest. Build. Thrive. – Book Cover Spread</title>
<link rel="stylesheet" href="https://fonts.googleapis.com/css2?family=Bebas+Neue&family=Montserrat:wght@400;500&display=swap">
<style>
  :root {
    --page-bg: #d4d4d4;
    --sky-top: #eef2f6;
    --sky-mid: #b9c7d6;
    --glow: #ffffff;
    --sea-light: #6f8fb0;
    --sea-mid: #2f5682;
    --sea-deep: #10263f;
    --night: #070d16;
    --wave-a: rgba(255, 255, 255, 0.22);
    --wave-b: rgba(150, 185, 220, 0.35);
    --wave-c: rgba(40, 80, 125, 0.55);
    --panel: rgba(8, 16, 28, 0.94);
    --ink-dark: #0c1a2b;
    --ink-light: #ffffff;
  }
  * { box-sizing: border-box; margin: 0; padding: 0; }
  html, body { width: 745px; height: 1200px; overflow: hidden; }
  body { background: var(--page-bg); position: relative; font-family: "Montserrat", sans-serif; }

  .cover-spread {
    position: absolute; left: 20px; top: 390px;
    width: 705px; height: 419px; overflow: hidden;
  }
  .cover-art {
    position: absolute; inset: 0;
    background:
      radial-gradient(ellipse 150px 95px at 78% 6%, var(--glow), transparent 72%),
      radial-gradient(ellipse 220px 160px at 82% 100%, var(--night), transparent 75%),
      radial-gradient(ellipse 260px 120px at 20% 100%, var(--night), transparent 80%),
      linear-gradient(180deg, var(--sky-top) 0%, var(--sky-mid) 28%, var(--sea-light) 48%, var(--sea-mid) 70%, var(--sea-deep) 88%, var(--night) 100%);
  }
  .wave-layer { position: absolute; left: 0; bottom: 0; width: 705px; height: 240px; }

  /* Back cover */
  .back-panel {
    position: absolute; left: 17px; top: 32px; width: 296px; height: 356px;
    background: var(--panel); color: var(--ink-light); padding: 0 15px 0 13px;
  }
  .back-title {
    font-family: "Bebas Neue", sans-serif; font-weight: 400;
    font-size: 24.5px; line-height: 1; letter-spacing: 0.2px; margin-top: 21px;
  }
  .back-summary, .author-bio {
    font-size: 8.3px; line-height: 10.4px; text-align: justify; letter-spacing: 0.05px;
  }
  .back-summary { margin-top: 7px; }
  .author-bio { margin-top: 33px; }
  .author-photo {
    float: left; width: 52px; height: 55px; margin: 1px 6px 0 0;
    background: linear-gradient(160deg, #d6d6d6, #6d6d6d);
  }
  .author-signature {
    position: absolute; right: 15px; top: 321px; font-size: 8.5px;
  }

  /* Spine */
  .spine-title {
    position: absolute; left: 336px; top: 33px;
    writing-mode: vertical-rl; white-space: nowrap;
    font-family: "Bebas Neue", sans-serif; font-size: 25px; line-height: 1;
    color: var(--ink-dark); letter-spacing: 0.3px;
  }
  .spine-author {
    position: absolute; left: 344px; top: 222px;
    writing-mode: vertical-rl; white-space: nowrap; font-size: 6px; color: var(--ink-light);
  }
  .spine-brand {
    position: absolute; left: 344px; top: 340px;
    writing-mode: vertical-rl; white-space: nowrap; font-size: 6px; font-weight: 500;
    color: var(--ink-light); display: flex; align-items: center; gap: 3px;
  }

  /* Front cover */
  .front-title {
    position: absolute; left: 420px; width: 245px; top: 28px; text-align: center;
    font-family: "Bebas Neue", sans-serif; font-size: 44px; line-height: 40px;
    color: var(--ink-dark); letter-spacing: 0.5px;
  }
  .front-subtitle {
    position: absolute; left: 420px; width: 245px; top: 113px; text-align: center;
    font-size: 6.6px; line-height: 8.3px; color: var(--ink-dark);
  }
  .front-brand {
    position: absolute; right: 12px; bottom: 7px; white-space: nowrap;
    display: flex; align-items: center; gap: 3px;
    font-size: 6.5px; font-weight: 500; color: var(--ink-light);
  }
  .brand-square { width: 6px; height: 6px; background: var(--ink-light); display: inline-block; }
</style>
</head>
<body>
  <section class="cover-spread">
    <div class="cover-art" role="img" aria-label="Misty mountain range with a person standing on a rocky summit, arms raised"></div>
    <svg class="wave-layer" viewBox="0 0 705 240" preserveAspectRatio="none" aria-hidden="true">
      <path d="M0 90 C90 60 180 120 270 90 S450 60 540 90 S660 120 705 95 L705 240 L0 240 Z" fill="var(--wave-a)"/>
      <path d="M0 130 C80 105 170 155 260 128 S440 100 530 130 S650 160 705 135 L705 240 L0 240 Z" fill="var(--wave-b)"/>
      <path d="M0 175 C100 150 190 200 290 172 S470 145 560 175 S660 200 705 180 L705 240 L0 240 Z" fill="var(--wave-c)"/>
      <path d="M0 112 C90 85 180 140 270 110 S450 82 540 112 S660 140 705 115" fill="none" stroke="rgba(255,255,255,0.45)" stroke-width="1"/>
    </svg>

    <article class="back-panel">
      <h2 class="back-title">REST BUILD THRIVE</h2>
      <p class="back-summary">Believe in you. Trust in You. Rest. Build. Thrive. is a book committed to you. You must feel empowered to make decisions and changes to improve your life and health. But, you may not always have the knowledge to do that. This book provides you with practical and fun tools and tips to improve your fitness level, healthy eating, and mental strength. You are awesome. You are beautiful. You have the power to control your destiny and future. All you have to do is Rest, Build, and Thrive!</p>
      <p class="author-bio"><span class="author-photo" role="img" aria-label="Portrait of the author"></span>Gregory Halvorsen is a Registered Dietitian and Certified Personal Trainer from Cleveland, OH. He graduated from the Westbrook Valley University and currently works as a health coach in the healthcare industry. His passions are fitness, nutrition, science, and motivation. He has extensive knowledge and experience in wellness, healthcare, and disease treatment and disease. Gregory has worked with hundreds of people through counseling, consulting, and coaching in an effort to make a difference in their long-term health. In his spare time, he enjoys exercising, watching movies, and trying out new foods</p>
      <p class="author-signature">Gregory Halvorsen RD, CPT</p>
    </article>

    <h2 class="spine-title">REST BUILD THRIVE</h2>
    <p class="spine-author">Gregory Halvorsen RD, CPT</p>
    <div class="spine-brand"><span class="brand-square"></span>REST BUILD THRIVE</div>

    <h1 class="front-title">REST BUILD<br>THRIVE</h1>
    <p class="front-subtitle">A Hands-On Diet, Fitness, and Attitude Handbook Building<br>Energy Toward Stronger Vitality and Balance</p>
    <div class="front-brand"><span class="brand-square"></span>REST BUILD THRIVE</div>
  </section>
</body>
</html>
```